Shipping Box & Supplies - Aquatics

Design shipping boxes and padded envelopes

Target Market(s)

Local Consumers

Industry/Entity Type

Tropical Fish/Aquatics

Requirements
Must have
• Logo, website and national telephone number
Nice to have
• Pictures attached
Should not have
• address

```html
<!DOCTYPE html>
<html lang="en">
<head>
<meta charset="UTF-8">
<title>Reefline Aquatics – Shipping Box</title>
<link rel="stylesheet" href="https://fonts.googleapis.com/css2?family=Michroma&family=Roboto:wght@500&display=swap">
<style>
  :root {
    --backdrop: #aee9fb;
    --box-blue: #0b3fd6;
    --box-blue-deep: #0a36b8;
    --flap-blue: #0e46dc;
    --ink-light: #f1f1ec;
    --sea-top: #2f7f95;
    --sea-mid: #3f98a4;
    --sea-floor: #3d4f66;
    --coral: #b86a9a;
  }
  * { margin: 0; padding: 0; box-sizing: border-box; }
  html, body { width: 1200px; height: 900px; overflow: hidden; }
  body {
    background: var(--backdrop);
    font-family: "Michroma", sans-serif;
    color: var(--ink-light);
    position: relative;
  }
  .dieline { position: absolute; left: 70px; top: 90px; width: 1060px; height: 720px; }

  /* top flap */
  .top-flap {
    position: absolute; left: 420px; top: 0; width: 640px; height: 230px;
    background: var(--flap-blue);
    display: flex; flex-direction: column; align-items: center; justify-content: center; gap: 10px;
  }
  .top-flap .brand-name { font-size: 26px; }
  .top-flap .contact { font-size: 9px; letter-spacing: 3px; line-height: 1.7; text-align: center; }

  /* end panel with underwater scene */
  .end-panel {
    position: absolute; left: 0; top: 240px; width: 410px; height: 480px; overflow: hidden;
  }
  .sea-scene {
    position: absolute; inset: 0;
    background: linear-gradient(180deg, var(--sea-top) 0%, var(--sea-mid) 45%, #4c7f8a 72%, var(--sea-floor) 100%);
  }
  .coral-bed {
    position: absolute; left: 0; right: 0; bottom: 0; height: 150px;
    background: linear-gradient(180deg, rgba(184,106,154,0) 0%, rgba(184,106,154,.45) 50%, rgba(61,79,102,.9) 100%);
  }
  .end-panel .brand {
    position: absolute; left: 28px; top: 40px;
  }
  .end-panel .brand-name { font-size: 30px; line-height: 1.1; }
  .end-panel .web { font-family: "Roboto", sans-serif; font-weight: 500; font-size: 15px; margin-top: 8px; }
  .photo {
    position: absolute; border-radius: 50%; border: 3px solid var(--ink-light);
  }
  .photo-coral   { left: 20px;  top: 170px; width: 110px; height: 110px; background: #3f8a6a; }
  .photo-anemone { left: 85px;  top: 215px; width: 145px; height: 145px; background: #8a5a7a; }
  .photo-shrimp  { left: 275px; top: 130px; width: 70px;  height: 70px;  background: #c9a9a4; }
  .photo-clown   { left: 290px; top: 185px; width: 110px; height: 110px; background: #c77a4a; }
  .photo-urchin  { left: 240px; top: 265px; width: 100px; height: 100px; background: #5d5f9a; }
  .photo-polyps  { left: 300px; top: 320px; width: 100px; height: 100px; background: #9a8fb8; }

  /* long panel */
  .long-panel {
    position: absolute; left: 420px; top: 240px; width: 640px; height: 480px;
    background: var(--box-blue);
    overflow: hidden;
  }
  .wave-field {
    position: absolute; left: 0; right: 0; bottom: 0; height: 300px;
    background: linear-gradient(180deg, rgba(10,54,184,0) 0%, var(--box-blue-deep) 100%);
  }
  .long-panel .brand {
    position: absolute; left: 0; right: 0; top: 120px; text-align: center;
  }
  .long-panel .brand-name { font-size: 46px; line-height: 1.25; }
  .long-panel .contact {
    margin-top: 26px; font-size: 16px; letter-spacing: 5px; line-height: 1.8;
  }
  .this-way-up { position: absolute; width: 30px; height: 46px; }
  .this-way-up.left  { left: 22px;  top: 28px; }
  .this-way-up.right { right: 22px; top: 28px; }
</style>
</head>
<body>
  <main class="dieline">
    <section class="top-flap">
      <div class="brand-name">REEFLINE AQUATICS</div>
      <div class="contact">WWW.REEFLINEAQUATICS.COM<br>+01 (555)010-2040</div>
    </section>

    <section class="end-panel">
      <div class="sea-scene" role="img" aria-label="Underwater reef scene with corals, seaweed and rippling light"></div>
      <div class="coral-bed" role="img" aria-label="Coral reef seabed"></div>
      <div class="brand">
        <div class="brand-name">REEFLINE<br>AQUATICS</div>
        <div class="web">www.reeflineaquatics.com</div>
      </div>
      <div class="photo photo-coral" role="img" aria-label="Photo of colourful zoanthid corals"></div>
      <div class="photo photo-anemone" role="img" aria-label="Photo of a purple anemone"></div>
      <div class="photo photo-shrimp" role="img" aria-label="Photo of a red cleaner shrimp"></div>
      <div class="photo photo-clown" role="img" aria-label="Photo of clownfish"></div>
      <div class="photo photo-urchin" role="img" aria-label="Photo of a sea urchin"></div>
      <div class="photo photo-polyps" role="img" aria-label="Photo of coral polyps"></div>
    </section>

    <section class="long-panel">
      <div class="wave-field" role="img" aria-label="Subtle wave pattern"></div>
      <svg class="this-way-up left" viewBox="0 0 30 46" aria-hidden="true">
        <path d="M15 0 L30 18 H21 V46 H9 V18 H0 Z" fill="var(--ink-light)"/>
      </svg>
      <svg class="this-way-up right" viewBox="0 0 30 46" aria-hidden="true">
        <path d="M15 0 L30 18 H21 V46 H9 V18 H0 Z" fill="var(--ink-light)"/>
      </svg>
      <div class="brand">
        <div class="brand-name">REEFLINE<br>AQUATICS</div>
        <div class="contact">WWW.REEFLINEAQUATICS.COM<br>+01 (555)010-2040</div>
      </div>
    </section>
  </main>
</body>
</html>
```